Brightwave Business Card

Professional Business Card Design required using the attached contact information.

Contact information can be rearranged as required.

The company is a new start up venture developing solar systems, the branding should be in keeping with that of one of the investors whose website is as follows https://www.quorvex.com/

```html
<!DOCTYPE html>
<html lang="en">
<head>
<meta charset="utf-8">
<title>Brightwave Renewables – Business Card</title>
<link rel="stylesheet" href="https://fonts.googleapis.com/css2?family=Lato:wght@700&family=Oswald:wght@500&family=Roboto+Slab:wght@400&display=swap">
<style>
  :root {
    --backdrop: #6f5236;
    --card-light: #ffffff;
    --card-dark: #0f0f0f;
    --ink: #1b1b1b;
    --accent: #2f5a4c;
    --decor-light: #e6e7e6;
    --decor-dark: #1c2421;
    --on-dark: #f2f2f2;
  }
  * { margin: 0; padding: 0; box-sizing: border-box; }
  html, body { width: 900px; height: 1200px; overflow: hidden; }
  body { background: var(--backdrop); position: relative; }

  .card {
    position: absolute;
    left: 85px;
    width: 728px;
    overflow: hidden;
    box-shadow: 0 6px 14px rgba(0,0,0,0.45);
  }
  .card--front { top: 145px; height: 425px; background: var(--card-light); }
  .card--back  { top: 623px; height: 427px; background: var(--card-dark); }

  .wordmark {
    position: absolute;
    font-family: "Lato", sans-serif;
    font-weight: 700;
    font-size: 24px;
    letter-spacing: 1.6px;
    white-space: nowrap;
  }
  .card--front .wordmark { right: 34px; top: 56px; color: var(--ink); }
  .card--back .wordmark { left: 0; right: 0; top: 210px; text-align: center; color: var(--on-dark); }

  .decor-circle { position: absolute; border-radius: 50%; }
  .card--front .decor-circle { width: 250px; height: 250px; left: 490px; top: 120px; background: var(--decor-light); }
  .card--back .decor-circle { width: 300px; height: 300px; left: 420px; top: 30px; background: var(--decor-dark); }

  .name-tag {
    position: absolute;
    left: 0; top: 244px;
    width: 203px; height: 32px;
    background: #000;
    color: #fff;
    font-family: "Oswald", sans-serif;
    font-weight: 500;
    font-size: 20px;
    letter-spacing: 0.5px;
    line-height: 32px;
    padding-left: 38px;
  }

  .contact-list { position: absolute; left: 36px; top: 292px; list-style: none; }
  .contact-list li {
    display: flex; align-items: center;
    height: 25px;
    font-family: "Roboto Slab", serif;
    font-size: 15.5px;
    color: var(--ink);
  }
  .contact-list svg { width: 14px; height: 14px; margin-right: 12px; fill: var(--accent); flex: none; }
</style>
</head>
<body>
  <section class="card card--front">
    <div class="decor-circle"></div>
    <div class="wordmark">BRIGHTWAVE RENEWABLES</div>
    <div class="name-tag">DANIEL CORWEN</div>
    <ul class="contact-list">
      <li>
        <svg viewBox="0 0 16 16" aria-hidden="true"><path d="M3.5 1.5l2.5 0 1.2 3.2-1.6 1.2c.8 1.8 2.2 3.2 4 4l1.2-1.6 3.2 1.2v2.5c0 .8-.7 1.5-1.5 1.5C6.6 13.5 2 8.9 2 3c0-.8.7-1.5 1.5-1.5z"/></svg>
        +1 (555) 214-0736
      </li>
      <li>
        <svg viewBox="0 0 16 16" aria-hidden="true"><path d="M1 3h14v10H1z M2.5 4.5v.4L8 8.7l5.5-3.8v-.4z" fill-rule="evenodd"/></svg>
        daniel.corwen@brightwave-renewables.com
      </li>
      <li>
        <svg viewBox="0 0 16 16" aria-hidden="true"><path d="M8 1a7 7 0 100 14A7 7 0 008 1zm0 1.3c.7.8 1.3 2.1 1.5 3.7h-3C6.7 4.4 7.3 3.1 8 2.3zM5.3 6H2.6a5.7 5.7 0 012.9-3.4C5.3 3.6 5.3 4.8 5.3 6zm0 1.3c0 1.2.1 2.4.3 3.4H2.6a5.7 5.7 0 010-3.4zm1.2 0h3c.1 1.2 0 2.4-.2 3.4H6.7c-.2-1-.3-2.2-.2-3.4zm4.2 0h2.7a5.7 5.7 0 010 3.4h-2.9c.2-1 .3-2.2.2-3.4zm0-1.3c0-1.2 0-2.4-.2-3.4A5.7 5.7 0 0113.4 6zM2.9 12h2.9c.2.6.4 1.1.6 1.6A5.7 5.7 0 012.9 12zm4.2 0h1.8c-.3.8-.6 1.4-.9 1.8-.3-.4-.6-1-.9-1.8zm3.1 0h2.9a5.7 5.7 0 01-3.5 1.6c.2-.5.4-1 .6-1.6z"/></svg>
        www.quorvex.com
      </li>
      <li>
        <svg viewBox="0 0 16 16" aria-hidden="true"><path d="M8 1a5 5 0 00-5 5c0 3.6 5 9 5 9s5-5.4 5-9a5 5 0 00-5-5zm0 7a2 2 0 110-4 2 2 0 010 4z"/></svg>
        118 Harbor Street, Portland, ME 04101
      </li>
    </ul>
  </section>

  <section class="card card--back">
    <div class="decor-circle"></div>
    <div class="wordmark">BRIGHTWAVE RENEWABLES</div>
  </section>
</body>
</html>
```